Inspirational quote for home gym wall - Desmond Okafor quote

I'd like to design a poster for my home gym with a quote from Desmond Okafor

"The fight is won or lost far away from witnesses - behind the lines, in the gym, and out there on the road, long before I dance under those lights."

The size should be approximately 1.5 x 2 m.

It's for inspiration to keep me going in my gym and there's noone better than Okafor. I will get it printed onto canvas. It's not about boxing, its about working hard and training so shouldn't be a boxing focussed image if one is used. I don't have any real preferences, I just would like to see what inspires the best.

Font styles to use
Sans Serif

Colors
000000
ffffff
fbed33

Requirements
Nice to have
• Maybe a black and white image of Okafor training in the background?
• Some thoughts on type of images (doesn't have to be these ones)
• https://www.stockvaultpix.example/detail/news-photo/american-heavyweight-boxing-champion-desmond-okafor-training-news-photo/90317452#/american-heavyweight-boxing-champion-desmond-okafor-training-at-picture-id90317452
• https://www.findlyquest.example/search?q=desmond+okafor+training&img=1#r=a1
• https://www.findlyquest.example/search?q=desmond+okafor+training&img=1#r=b2
• https://www.findlyquest.example/search?q=desmond+okafor+training&img=1#r=c3
• https://www.findlyquest.example/search?q=desmond+okafor+training&img=1#r=d4
• https://www.findlyquest.example/search?q=desmond+okafor+training&img=1#r=e5
• The more designs I see, the more I prefer black and white with maybe only a bit of colour such as gold.
Should not have
• I'm not a fan of red

```html
<!DOCTYPE html>
<html lang="en">
<head>
<meta charset="utf-8">
<title>The Fight Is Won or Lost – Gym Poster</title>
<link href="https://fonts.googleapis.com/css2?family=Archivo:wdth,wght@62..125,100..900&display=swap" rel="stylesheet">
<style>
  :root {
    --canvas-black: #262626;
    --quote-yellow: #f4ea3a;
    --photo-light: #bdbdbd;
    --photo-mid: #7a7a7a;
    --photo-dark: #3a3a3a;
  }
  html, body {
    margin: 0;
    padding: 0;
    width: 900px;
    height: 1200px;
    overflow: hidden;
    background: var(--canvas-black);
  }
  .poster {
    display: block;
    width: 900px;
    height: 1200px;
  }
  .quote-line {
    fill: var(--quote-yellow);
    font-family: "Archivo", "Arial Black", sans-serif;
    font-weight: 900;
    font-stretch: 125%;
    font-variation-settings: "wdth" 125;
  }
  .quote-line--narrow {
    font-weight: 700;
    font-stretch: 88%;
    font-variation-settings: "wdth" 88;
  }
  .quote-line--bold {
    font-weight: 800;
    font-stretch: 100%;
    font-variation-settings: "wdth" 100;
  }
</style>
</head>
<body>
<svg class="poster" viewBox="0 0 900 1200" xmlns="http://www.w3.org/2000/svg">
  <defs>
    <filter id="canvas-grain" x="0" y="0" width="100%" height="100%">
      <feTurbulence type="fractalNoise" baseFrequency="0.9" numOctaves="2" seed="3" result="noise"/>
      <feColorMatrix in="noise" type="matrix"
        values="0 0 0 0 0.16  0 0 0 0 0.16  0 0 0 0 0.16  0 0 0 1.4 -0.35"/>
    </filter>
    <filter id="distress" x="-5%" y="-5%" width="110%" height="110%">
      <feTurbulence type="fractalNoise" baseFrequency="0.55" numOctaves="2" seed="8" result="speckle"/>
      <feColorMatrix in="speckle" type="matrix"
        values="0 0 0 0 0  0 0 0 0 0  0 0 0 0 0  0 0 0 -9 6.2" result="holes"/>
      <feComposite in="SourceGraphic" in2="holes" operator="in"/>
    </filter>
    <radialGradient id="photo-tone" cx="0.5" cy="0.4" r="0.7">
      <stop offset="0" stop-color="var(--photo-light)"/>
      <stop offset="0.6" stop-color="var(--photo-mid)"/>
      <stop offset="1" stop-color="var(--photo-dark)"/>
    </radialGradient>
  </defs>

  <rect class="canvas-ground" width="900" height="1200" fill="var(--canvas-black)"/>
  <rect class="canvas-texture" width="900" height="1200" filter="url(#canvas-grain)"/>

  <rect class="training-photo" role="img"
        aria-label="Black and white photo of Desmond Okafor in training"
        x="300" y="130" width="360" height="1010"
        fill="url(#photo-tone)" opacity="0.7"/>

  <g class="quote" filter="url(#distress)">
    <text class="quote-line" x="44" y="112" font-size="110" textLength="796" lengthAdjust="spacingAndGlyphs">THE FIGHT IS</text>
    <text class="quote-line" x="44" y="240" font-size="72" textLength="240" lengthAdjust="spacingAndGlyphs">WON</text>
    <text class="quote-line" x="312" y="220" font-size="34" textLength="80" lengthAdjust="spacingAndGlyphs">OR</text>
    <text class="quote-line" x="592" y="240" font-size="72" textLength="268" lengthAdjust="spacingAndGlyphs">LOST</text>
    <text class="quote-line quote-line--narrow" x="36" y="342" font-size="56" textLength="804" lengthAdjust="spacingAndGlyphs">FAR AWAY FROM WITNESSES -</text>
    <text class="quote-line quote-line--bold" x="60" y="478" font-size="140" textLength="768" lengthAdjust="spacingAndGlyphs">IN THE GYM,</text>
    <text class="quote-line quote-line--bold" x="40" y="580" font-size="84" textLength="792" lengthAdjust="spacingAndGlyphs">BEHIND THE LINES,</text>
    <text class="quote-line" x="44" y="676" font-size="56" textLength="756" lengthAdjust="spacingAndGlyphs">AND OUT THERE</text>
    <text class="quote-line" x="48" y="776" font-size="88" textLength="800" lengthAdjust="spacingAndGlyphs">ON THE ROAD,</text>
    <text class="quote-line" x="44" y="868" font-size="84" textLength="796" lengthAdjust="spacingAndGlyphs">LONG BEFORE</text>
    <text class="quote-line" x="44" y="956" font-size="84" textLength="796" lengthAdjust="spacingAndGlyphs">I DANCE</text>
    <text class="quote-line" x="44" y="1028" font-size="78" textLength="796" lengthAdjust="spacingAndGlyphs">UNDER THOSE</text>
    <text class="quote-line" x="44" y="1144" font-size="128" textLength="792" lengthAdjust="spacingAndGlyphs">LIGHTS</text>
  </g>
</svg>
</body>
</html>
```